Wordpress Web Design For Midlifers.com

We're looking to update the design for www.midlifers.com. The website provides news and views for people aged 50 plus.

We want to use Wordpress as the content management tool and incorporate mailchimp to manage subscribers to our monthly newsletter.

In terms of design, we're looking for something simple and straightforward, we quite like the elder hub site, so something like that would be good. http://www.elderhub.org.uk
Updates

Project Deadline Extended
Reason: Dear All, Due to the Xmas break in the UK I've decided to extend the deadline by 7 days. Thanks for all your submissions, we will be making a decision shortly. Please note, as per the original brief, we are only interested in fully coded sites uploaded to our hosting provider. Please withdraw your design if you are not able to offer this complete solution. Thanks and good wishes to all!

Requirements
Must have
• Fully working wordpress templates that allow us to easily manage the website content. Easy for readers to use, navigate and read the content.
• Ideally a'turnkey' solution - the website built and ready for us to use wordpress to populate with content.

```html
<!DOCTYPE html>
<html lang="en">
<head>
<meta charset="utf-8">
<title>Midlifers.com – The New Generation</title>
<link rel="stylesheet" href="https://fonts.googleapis.com/css2?family=Open+Sans:wght@400;600;700&family=Arimo:wght@400;700&family=Noto+Sans:wght@400;700&display=swap">
<style>
:root{
  --green:#8cb82b;
  --green-dark:#5e8f1f;
  --green-text:#6a9a12;
  --ink:#333;
  --grey:#777;
  --light:#aaa;
  --footer:#2e2e2e;
  --nav-dark:#222;
}
*{margin:0;padding:0;box-sizing:border-box}
html,body{width:742px;height:1200px;overflow:hidden;background:#fff}
body{position:relative;font-family:"Open Sans",sans-serif;color:var(--ink)}
.abs{position:absolute}
.topline{left:0;top:0;width:742px;height:4px;background:var(--green)}
.brand{left:84px;top:22px;display:flex;align-items:center;gap:8px}
.brand-dot{width:44px;height:44px;border-radius:50%;background:var(--green)}
.brand-name{font-size:19px;font-weight:600;color:#444}
.phone{left:505px;top:21px;font-family:"Arimo",sans-serif;font-size:15px;color:var(--green)}
.help{left:620px;top:20px;width:60px;height:18px;border-radius:3px;background:var(--green);color:#fff;font-size:7.5px;font-family:"Arimo",sans-serif;text-align:center;line-height:18px}
.search{left:519px;top:55px;width:162px;height:19px;border:1px solid #ddd;font-size:8px;color:#999;font-style:italic;padding:4px 7px}
.search-btn{left:663px;top:55px;width:18px;height:19px;background:#555}
.nav{left:54px;top:89px;width:688px;height:31px;background:var(--green);display:flex;font-family:"Arimo",sans-serif;font-size:11px;color:#fff}
.nav a{color:#fff;text-decoration:none;line-height:31px;padding:0 0 0 0}
.nav .home{background:var(--nav-dark);width:60px;text-align:center}
.hero-photo{left:0;top:121px;width:493px;height:202px;background:linear-gradient(120deg,#d9d3cb,#c7b8a8 45%,#e6e2dc)}
.hero-caption{left:0;top:275px;width:493px;height:48px;background:rgba(168,200,100,.55)}
.dots{left:33px;top:296px;display:flex;gap:3px}
.dots span{width:8px;height:8px;border-radius:50%;background:#fff}
.dots span:first-child{background:var(--green)}
.hero-title{left:131px;top:287px;font-family:"Noto Sans",sans-serif;font-size:19px;color:#333}
.sub{left:493px;top:121px;width:249px;height:202px;background:linear-gradient(#6f9e1f,#5a8a18)}
.sub h2{position:absolute;left:25px;top:18px;font-size:15px;font-weight:400;color:#fff;line-height:21px}
.sub h2 b{color:#d4ec7a;font-weight:600}
.sub p{position:absolute;left:29px;top:74px;width:125px;font-size:9px;color:#fff;letter-spacing:.6px;line-height:11.5px}
.sub .mail{position:absolute;left:160px;top:72px}
.sub .email{position:absolute;left:30px;top:162px;width:146px;height:20px;background:#fff;border-radius:2px 0 0 2px;font-size:7.5px;color:#888;padding:5px 10px}
.sub .go{position:absolute;left:168px;top:162px;width:20px;height:20px;background:#555}
.col h3{font-size:13px;font-weight:400;color:#444;line-height:15.5px;letter-spacing:.4px}
.about h3{color:var(--green-text);font-size:14px}
.copy{font-size:10px;color:var(--grey);letter-spacing:.7px;line-height:11.6px}
.copy.faint{color:#999}
.more{font-size:10px;font-weight:700;color:var(--green-text);letter-spacing:1px}
.frame{border:4px solid #f0f0f0;background:#fff}
.ph{display:block;width:100%;height:100%}
.side-donate{left:496px;top:340px;width:193px;height:161px}
.donate-photo{height:88px;background:linear-gradient(135deg,#eee7de,#cdbcaa)}
.donate-body{height:73px;background:linear-gradient(#8cb82b,#6f9e1f);padding:8px 14px;color:#fff}
.donate-body b{font-size:10.5px;letter-spacing:.8px}
.donate-body p{font-size:8.5px;letter-spacing:.7px;line-height:12.8px;margin-top:1px}
.donate-body .now{position:absolute;right:6px;bottom:6px;font-size:8.5px;color:#d8efa0;letter-spacing:.7px}
.smile{left:496px;top:518px;width:193px;height:165px;background:linear-gradient(135deg,#d8c2b5,#b3898a 60%,#c84b5a)}
.smile .tag{position:absolute;left:6px;top:118px;background:#8d1a5d;color:#fff;padding:1px 4px;font-size:14px;line-height:17px}
.smile .tag b{display:block;font-size:16px}
.smile .badge{position:absolute;left:130px;top:104px;width:56px;height:56px;border-radius:50%;background:#8d1a5d;border:2px solid #fff;color:#fff;font-size:8px;font-weight:700;text-align:center;line-height:9px;padding-top:16px}
.kindred{left:496px;top:711px;width:193px;height:149px;border:1px solid #ccc;background:#fff;text-align:center}
.kindred .dot{width:26px;height:26px;border-radius:50%;background:#7a2a8c;margin:30px auto 8px}
.kindred .name{font-size:30px;color:#333;line-height:32px}
.kindred .sub2{font-size:14px;color:#333}
.hosting{left:496px;top:872px;width:193px;height:175px;border-radius:6px;background:linear-gradient(#3a3a3a,#1f1f1f);color:#fff;font-family:"Arimo",sans-serif;font-weight:700;padding:0 12px}
.hosting .l1{margin-top:46px;font-size:15px}
.hosting .l2{font-size:27px;line-height:30px}
.hosting .l3{font-size:13px;margin-top:3px}
.hosting .cta{position:absolute;left:15px;top:134px;width:100px;height:22px;border-radius:11px;background:var(--green);border:2px solid #fff;font-size:12px;line-height:18px;padding-left:9px}
.banner{left:66px;top:1030px;width:374px;height:48px;border:1px solid #ddd;background:linear-gradient(90deg,#dde4ee,#fff 35%)}
.banner .pic{position:absolute;left:0;top:0;width:64px;height:46px;background:linear-gradient(135deg,#c6d0da,#a9b8c8)}
.banner .t1{position:absolute;left:116px;top:9px;font-size:15px;font-weight:700;color:#8d1a5d;line-height:16px}
.banner .t2{position:absolute;left:116px;top:25px;font-size:16px;color:#2aa6d8}
.banner .b{position:absolute;left:320px;top:16px;font-size:10px;color:#333}
.footer{left:0;top:1105px;width:742px;height:95px;background:var(--footer);border-top:3px solid #ccc}
.links{position:absolute;left:63px;font-size:8.5px;color:#fff;word-spacing:1px}
.links span{margin:0 6px;color:#ccc}
.copyright{position:absolute;left:63px;top:61px;font-size:8.5px;color:#666}
.copyright em{font-style:normal;color:var(--green)}
.social{position:absolute;left:629px;top:26px;display:flex;gap:5px}
.social i{width:15px;height:15px;border-radius:2px}
</style>
</head>
<body>
<div class="abs topline"></div>

<header>
  <div class="abs brand"><span class="brand-dot"></span><span class="brand-name">Midlifers.com</span></div>
  <div class="abs phone">+01632 960418</div>
  <div class="abs help">Need Help ?</div>
  <div class="abs search">Search here</div>
  <div class="abs search-btn"><svg width="18" height="19"><path d="M7 6l4 3.5-4 3.5z" fill="#fff"/></svg></div>
  <nav class="abs nav">
    <a class="home">Home</a>
    <a style="margin-left:25px">Travel</a>
    <a style="margin-left:41px">Health</a>
    <a style="margin-left:41px">Hobbies</a>
    <a style="margin-left:34px">Lifestyle</a>
    <a style="margin-left:37px">Insurance</a>
    <a style="margin-left:34px">Legal</a>
    <a style="margin-left:38px">Competitions</a>
    <a style="margin-left:31px">Survey</a>
  </nav>
</header>

<section>
  <div class="abs hero-photo" role="img" aria-label="Smiling older couple outdoors, the man pointing into the distance"></div>
  <div class="abs hero-caption"></div>
  <div class="abs dots"><span></span><span></span><span></span><span></span></div>
  <div class="abs hero-title">Age no bar for Pursuit of Happiness</div>

  <div class="abs sub">
    <h2>Subscribe to the<br><b>Weekly Newsletters</b></h2>
    <p>Keep up to date Sign up for our fortnightly newsletter</p>
    <svg class="mail" width="60" height="60" viewBox="0 0 60 60" aria-hidden="true">
      <rect x="6" y="18" width="46" height="32" rx="3" fill="#e8f2fb" stroke="#3a8fd0" stroke-width="2"/>
      <path d="M6 19l23 18 23-18" fill="none" stroke="#3a8fd0" stroke-width="2"/>
      <circle cx="36" cy="16" r="10" fill="none" stroke="#fff" stroke-width="2"/>
    </svg>
    <div class="email">email address</div>
    <div class="go"><svg width="20" height="20"><path d="M8 6l5 4-5 4z" fill="#fff"/></svg></div>
  </div>
</section>

<main>
  <article class="abs col about" style="left:49px;top:345px;width:400px">
    <h3 style="margin-left:3px">About Midlifers</h3>
    <p class="copy" style="width:212px;margin-top:4px">We believe that age needs respect. It needs kindness. Sometimes it needs help. Because there is strength in numbers, Senior Care Trust and Later Life Aid have joined forces to become Elder Hub – so that we can be here for everyone in later life.</p>
    <p class="copy" style="width:212px;margin-top:11px">Want to know what Elder Hub is up to? Listen to our weekly podcast called Agenda.</p>
    <p class="more" style="margin-top:13px;margin-left:1px">Readmore</p>
  </article>
  <div class="abs frame" style="left:271px;top:369px;width:168px;height:138px"><div class="ph" role="img" aria-label="Group of cheerful seniors giving thumbs up" style="background:linear-gradient(135deg,#e2dbd2,#b8a795)"></div></div>

  <article class="abs col" style="left:50px;top:557px;width:400px">
    <h3>Top Ten Tips for keeping homes warm and energy bills down</h3>
    <p class="copy faint" style="width:206px;margin-top:13px">Four of the big six energy companies have hiked up prices before the seasonal surge in demand, and a survey for Elder Hub found that 28 per cent of pensioners said they were worrying about heating their homes during the winter. Dean Marlowe, Operations Director at central heating firm KPL Building Services, based near Ashfield Green, offers his Top Ten Tips for keeping homes warm and energy bills down:</p>
    <p class="more" style="margin-top:10px;margin-left:1px">Readmore</p>
  </article>
  <div class="abs frame" style="left:280px;top:596px;width:173px;height:141px"><div class="ph" role="img" aria-label="House-shaped energy efficiency rating chart from green A to red G" style="background:linear-gradient(90deg,#fff,#e6f0d8 40%,#f4d9b0 70%,#f0c0b8)"></div></div>

  <article class="abs col" style="left:50px;top:801px;width:400px">
    <h3>Top Ten Tips for keeping homes warm and energy bills down</h3>
    <p class="copy faint" style="width:206px;margin-top:13px">Four of the big six energy companies have hiked up prices before the seasonal surge in demand, and a survey for Elder Hub found that 28 per cent of pensioners said they were worrying about heating their homes during the winter. Dean Marlowe, Operations Director at central heating firm KPL Building Services, based near Ashfield Green, offers his Top Ten Tips for keeping homes warm and energy bills down:</p>
    <p class="more" style="margin-top:10px;margin-left:1px">Readmore</p>
  </article>
  <div class="abs frame" style="left:280px;top:840px;width:173px;height:141px"><div class="ph" role="img" aria-label="House-shaped energy efficiency rating chart from green A to red G" style="background:linear-gradient(90deg,#fff,#e6f0d8 40%,#f4d9b0 70%,#f0c0b8)"></div></div>

  <div class="abs banner">
    <div class="pic" role="img" aria-label="Happy older couple"></div>
    <div class="t1">over 50s life cover</div>
    <div class="t2">that ticks more boxes</div>
    <div class="b">Kindred</div>
  </div>
</main>

<aside>
  <div class="abs side-donate">
    <div class="donate-photo" role="img" aria-label="Grandfather with grandchild and young woman smiling"></div>
    <div class="donate-body">
      <b>Donate</b>
      <p>Help us reach the thousands of older people who feel isolated and alone.</p>
      <span class="now">Donate Now &gt;&gt;</span>
    </div>
  </div>

  <div class="abs smile" role="img" aria-label="Elderly woman smiling at a festive party">
    <div class="tag">Raise a smile<b>#Voteelderhub</b></div>
    <div class="badge">NEVER<br>BE<br>LONELY</div>
  </div>

  <div class="abs kindred">
    <div class="dot"></div>
    <div class="name">Kindred</div>
    <div class="sub2">Mutual Assurance</div>
  </div>

  <div class="abs hosting">
    <div class="l1">Fast and Reliable</div>
    <div class="l2">Web Hosting</div>
    <div class="l3">Domain Name Included!</div>
    <div class="cta">Get Started ›</div>
  </div>
</aside>

<footer class="abs footer">
  <div class="links" style="top:28px">Home<span>|</span>Travel<span>|</span>Health<span>|</span>Hobbies<span>|</span>Lifestyle<span>|</span>Insurance<span>|</span>Legal<span>|</span>Competitions<span>|</span>Survey</div>
  <div class="links" style="top:43px">About Midlifers<span>|</span>Privacy Policy<span>|</span>Terms and Conditions<span>|</span>Advertise!<span>|</span>Contact Us</div>
  <div class="copyright">Copyright midlifers.com 2001-2013 &nbsp;&nbsp;&nbsp; Designed <em>Brightframe</em></div>
  <div class="social"><i style="background:#999"></i><i style="background:#3f62a8"></i><i style="background:#3fa9e0"></i></div>
</footer>
</body>
</html>
```